Brightoakrx website

We are a weight loss clinic and we need a website built. please look at these websites for content and style. Just need like 5 pages see samples. AI files of logo are not avail yet so use sample for place set

https://slimshiftstudio.example/
qorvatherapy.example
https://pinecrestclinicalbodybalance.example/
https://yourslimmingcorner.example/
https://krvskincare.example/treatments/weight-loss-injections/

Target Market(s)

Women

Industry/Entity Type

weight loss

Coding

Coded - Design and coding required

Number of Pages Required

5+ page

Requirements
Nice to have
• please make look like a medspa website

```html
<!DOCTYPE html>
<html lang="en">
<head>
<meta charset="utf-8">
<title>Brightoakrx — Weight Loss, Wellness, Rejuvenation</title>
<link href="https://fonts.googleapis.com/css2?family=Noto+Serif:wght@400;700&family=Roboto:wght@400;500;700&family=Poppins:wght@400;500;600&family=Great+Vibes&display=swap" rel="stylesheet">
<style>
:root{
  --green:#7ab55c;
  --green-dark:#5f9c43;
  --blue:#1f7ea1;
  --navy:#1d4f86;
  --ink:#222;
  --text:#555;
  --muted:#888;
  --band:#eef5e8;
  --footer:#222d3b;
  --white:#fff;
}
*{margin:0;padding:0;box-sizing:border-box}
html,body{width:1200px;height:3574px;overflow:hidden}
body{position:relative;background:var(--white);font-family:"Roboto",sans-serif;color:var(--text)}
.abs{position:absolute}
.serif{font-family:"Noto Serif",serif}
.script{font-family:"Great Vibes",cursive}
.photo{position:absolute;border-radius:50%}
.bubble{position:absolute;border-radius:50%;filter:blur(1px)}

/* header */
.hero{position:absolute;left:0;top:0;width:1200px;height:580px;background:linear-gradient(120deg,#f6f8fa 0%,#eaf1f6 60%,#f4f7f2 100%)}
.brand{position:absolute;left:160px;top:34px;display:flex;align-items:center;gap:10px}
.brand-dot{width:38px;height:38px;border-radius:50%;background:var(--blue)}
.brand-name{font-family:"Noto Serif",serif;font-size:30px;color:var(--green-dark);font-weight:400}
.nav{position:absolute;top:47px;left:481px;display:flex;gap:26px;font-size:13px;color:#444}
.nav .active{color:var(--green-dark)}
.book{position:absolute;left:914px;top:35px;width:124px;height:42px;border-radius:0 21px 21px 0;background:var(--green);color:#fff;font-size:13px;line-height:42px;text-align:center;border-left:3px solid var(--green-dark)}
.hero-kicker{left:161px;top:291px;font-size:24px;color:var(--green)}
.hero-title{left:161px;top:322px;font-size:37px;font-weight:700;color:var(--ink);white-space:nowrap}
.hero-copy{left:161px;top:381px;width:420px;font-size:11.5px;line-height:17px}
.btn{position:absolute;border-radius:22px;font-size:12px;font-weight:500;text-align:center;color:#fff}
.btn-blue{background:var(--blue)}
.card-badge{position:absolute;background:#fff;box-shadow:0 6px 18px rgba(0,0,0,.12);border-radius:3px;font-family:"Poppins",sans-serif}
.card-badge .dot{position:absolute;right:8px;top:8px;width:6px;height:6px;border-radius:50%;background:var(--green)}
.badge-ic{position:absolute;border-radius:50%;background:#e8eef2}

/* program */
.sec-title{position:absolute;left:0;width:1200px;text-align:center}
.prog-card{position:absolute;top:829px;width:256px;height:175px;background:#fff;box-shadow:0 5px 16px rgba(0,0,0,.12);padding:16px 15px}
.prog-card .ic{width:34px;height:34px;border-radius:50%;background:#e6f0df;margin-bottom:8px}
.prog-card h3{font-family:"Noto Serif",serif;font-weight:400;font-size:14.5px;color:var(--ink);margin-bottom:12px;white-space:nowrap;letter-spacing:-.2px}
.prog-card p{font-size:11px;line-height:14px;color:var(--muted)}

/* welcome */
.pill{font-family:"Poppins",sans-serif;font-size:11px;color:#333;padding-left:44px;line-height:44px;height:44px}

/* beauty */
.band{position:absolute;left:0;top:1686px;width:1200px;height:385px;background:linear-gradient(180deg,#fff 0%,var(--band) 100%)}
.svc{position:absolute;display:flex;align-items:center;gap:14px;font-family:"Poppins",sans-serif;font-size:15px;color:#333}
.svc .disc{width:66px;height:66px;border-radius:50%;background:#fff;box-shadow:0 4px 14px rgba(0,0,0,.12);display:flex;align-items:center;justify-content:center}
.svc .disc i{width:30px;height:30px;border-radius:50%;background:#f6dcd6;display:block}

/* events */
.event{position:absolute;top:2208px;width:240px;text-align:center}
.event .ph{width:176px;height:176px;border-radius:50%;margin:0 auto 26px}
.event h4{font-family:"Noto Serif",serif;font-weight:400;font-size:15px;color:#333;line-height:20px}
.event .when{font-size:8.5px;color:#666;margin:6px 0 14px}
.event p{font-size:10.5px;line-height:14.5px;color:#666}

/* stories */
.story{position:absolute;border-radius:50%;border:5px solid;border-color:var(--green) #b9dca4 transparent #b9dca4}
.field{position:absolute;top:3171px;width:249px;height:44px;border-radius:22px;background:#fff;box-shadow:0 3px 12px rgba(0,0,0,.07);font-size:11px;color:#777;padding-left:30px;line-height:44px}

/* footer */
.footer{position:absolute;left:0;top:3373px;width:1200px;height:201px;background:var(--footer);color:#fff}
.f-btn{position:absolute;top:34px;height:38px;border-radius:19px;background:var(--green);font-size:11px;line-height:38px;text-align:center;letter-spacing:.5px;white-space:nowrap}
.social{position:absolute;top:35px;width:34px;height:34px;border-radius:50%;border:1.5px solid #fff}
.f-nav{position:absolute;top:97px;left:0;width:1200px;display:flex;justify-content:center;gap:30px;font-size:12px}
.f-rule{position:absolute;left:160px;top:139px;width:878px;height:1px;background:#3a4656}
.copy{position:absolute;top:163px;left:0;width:1200px;text-align:center;font-size:8.5px;color:#c9ced6}
</style>
</head>
<body>

<!-- HERO -->
<section class="hero">
  <div class="bubble" style="left:-30px;top:85px;width:88px;height:88px;background:radial-gradient(circle,#d3ebf7,#e8f4fb)"></div>
  <div class="bubble" style="left:1020px;top:448px;width:115px;height:115px;background:radial-gradient(circle at 30% 30%,#fff,#e4eedc)"></div>
</section>

<header>
  <div class="brand"><span class="brand-dot"></span><span class="brand-name">Brightoakrx</span></div>
  <nav class="nav"><span class="active">HOME</span><span>ABOUT US</span><span>OUR SERVICES</span><span>BLOG</span><span>CONTACT US</span></nav>
  <div class="book">BOOK ONLINE</div>
</header>

<div class="abs serif hero-kicker">You Can Transform Health</div>
<h1 class="abs serif hero-title">Through Habit Change!</h1>
<p class="abs hero-copy">Nam eu volutpat orci, quis accumsan dui. Curabitur finibus scelerisque dolor, non tincidunt nibh vehicula eu. Integer massa arcu, lobortis ac tincidunt vel, tincidunt eget orci. Vestibulum ut consequat</p>
<div class="btn btn-blue" style="left:161px;top:452px;width:174px;height:40px;line-height:40px">Make an Appointment</div>

<svg class="abs" style="left:570px;top:110px" width="475" height="475" viewBox="0 0 475 475">
  <defs><linearGradient id="ring1" x1="0" y1="1" x2="1" y2="0"><stop offset="0" stop-color="#6ec3c9"/><stop offset="1" stop-color="#7ab55c"/></linearGradient></defs>
  <circle cx="237" cy="237" r="228" fill="none" stroke="#d9e8d0" stroke-width="2"/>
  <path d="M237 9 A228 228 0 0 1 237 465" fill="none" stroke="url(#ring1)" stroke-width="14" stroke-linecap="round"/>
</svg>
<div class="photo" style="left:617px;top:157px;width:380px;height:380px;background:radial-gradient(circle at 55% 40%,#c9a48a,#6b5a52 70%,#3c3432)" role="img" aria-label="Smiling woman eating a fruit salad"></div>

<div class="card-badge" style="left:530px;top:215px;width:140px;height:62px"><span class="dot"></span>
  <span class="badge-ic" style="left:6px;top:28px;width:22px;height:22px"></span>
  <div style="position:absolute;left:35px;top:12px;font-size:12px;font-weight:600;color:var(--blue);line-height:15px">Special<br><span style="font-weight:400;color:#333">Treatment</span></div>
  <div style="position:absolute;left:35px;top:46px;width:90px;height:4px;background:#eee;border-radius:2px"></div>
</div>
<div class="card-badge" style="left:908px;top:162px;width:125px;height:46px"><span class="dot"></span>
  <span class="badge-ic" style="left:14px;top:12px;width:22px;height:22px;background:#cfe2f0"></span>
  <div style="position:absolute;left:42px;top:10px;font-size:11px;line-height:13px;color:#333"><b style="color:var(--blue)">+3,000</b><br>Customer</div>
</div>
<div class="card-badge" style="left:577px;top:499px;width:139px;height:60px"><span class="dot"></span>
  <span class="badge-ic" style="left:10px;top:20px;width:22px;height:22px;background:#d5ebcb"></span>
  <div style="position:absolute;left:39px;top:9px;font-size:12px;font-weight:600;color:var(--blue);line-height:15px">Extraordinary<br><span style="font-weight:400;color:#333">Experience</span></div>
  <div style="position:absolute;left:39px;top:42px;width:80px;height:4px;background:#eee;border-radius:2px"></div>
</div>

<!-- PROGRAM -->
<div class="sec-title serif" style="top:659px;font-size:20px;color:#333">Medically Supervised</div>
<div class="sec-title" style="top:684px"><span class="script" style="font-size:36px;color:var(--blue);margin-right:10px">Weight Loss</span><span class="serif" style="font-size:30px;font-weight:700;color:var(--blue)">Program</span></div>
<p class="sec-title" style="top:741px;font-size:11.5px;line-height:16.5px;padding:0 295px">Nam eu volutpat orci, quis accumsan dui. Curabitur finibus scelerisque dolor, non tincidunt nibh vehicula eu. Integer massa arcu, lobortis ac tincidunt vel, tincidunt eget orci. Vestibulum ut consequat tellus, sed sodales orci. Interdum et malesuada fames ac ante ipsum</p>

<div class="prog-card" style="left:192px"><div class="ic"></div><h3>Weight Loss</h3><p>Nam eu volutpat orci, quis accumsan dui. Curabitur finibus scelerisque dolor, non tincidunt nibh vehicula eu. Integer massa arcu, lobortis</p></div>
<div class="prog-card" style="left:472px"><div class="ic"></div><h3>Aesthetic Treatments</h3><p>Nam eu volutpat orci, quis accumsan dui. Curabitur finibus scelerisque dolor, non tincidunt nibh vehicula eu. Integer massa arcu, lobortis</p></div>
<div class="prog-card" style="left:752px"><div class="ic"></div><h3>Hormone Replacement Therapy</h3><p>Nam eu volutpat orci, quis accumsan dui. Curabitur finibus scelerisque dolor, non tincidunt nibh vehicula eu. Integer massa arcu, lobortis</p></div>

<!-- WELCOME -->
<div class="photo" style="left:228px;top:1095px;width:320px;height:320px;background:#f1f1f1"></div>
<svg class="abs" style="left:160px;top:1240px" width="445" height="240" viewBox="0 0 445 240">
  <defs><linearGradient id="teal" x1="0" y1="0" x2="1" y2="1"><stop offset="0" stop-color="#5fc0c0"/><stop offset="1" stop-color="#8bc56e"/></linearGradient></defs>
  <path d="M0 25 Q0 0 40 0 L130 0 L130 200 Q30 200 0 110 Z" fill="url(#teal)"/>
  <path d="M440 0 Q445 170 340 230 L320 80 Q360 10 440 0 Z" fill="#7ab55c"/>
</svg>
<div class="photo" style="left:198px;top:1130px;width:370px;height:382px;border-radius:50% 50% 48% 48%;background:radial-gradient(circle at 50% 30%,#d4a98d,#8a6f62 60%,#b8c4cc)" role="img" aria-label="Smiling woman holding a bowl of salad"></div>
<div class="card-badge pill" style="left:448px;top:1103px;width:136px"><span class="dot"></span><span class="badge-ic" style="left:10px;top:9px;width:26px;height:26px"></span>Nutrition Plans</div>
<div class="card-badge pill" style="left:100px;top:1315px;width:134px"><span class="dot"></span><span class="badge-ic" style="left:10px;top:9px;width:26px;height:26px;background:#d5ebcb"></span>Natural Foods</div>
<div class="card-badge pill" style="left:465px;top:1438px;width:136px"><span class="dot"></span><span class="badge-ic" style="left:10px;top:9px;width:26px;height:26px;background:#d7ebf4"></span>Daily Exercise</div>

<div class="abs script" style="left:656px;top:1137px;font-size:36px;color:var(--blue)">Welcome to</div>
<h2 class="abs serif" style="left:656px;top:1172px;font-size:40px;font-weight:700;color:var(--ink)">Brightoakrx</h2>
<div class="abs" style="left:657px;top:1226px;width:26px;height:2px;background:#333"></div>
<p class="abs" style="left:656px;top:1240px;width:395px;font-size:11.5px;line-height:16.5px">Aenean vitae magna sagittis velit condimentum ultricies ut blandit mauris. Nullam facilisis dolor et metus tristique imperdiet. Fusce sit amet eros eu nisl feugiat molestie ac quis libero.</p>
<p class="abs" style="left:656px;top:1305px;width:400px;font-size:11.5px;line-height:16.5px">Vestibulum quam justo, euismod ac lacus in, finibus fermentum tellus. Duis risus odio, commodo et felis vel, malesuada ultrices leo. Etiam tincidunt lacus at magna ultrices, sagittis placerat lectus consequat. Nunc non finibus fermentum.</p>
<div class="btn btn-blue" style="left:656px;top:1394px;width:114px;height:38px;line-height:38px">Learn More</div>
<div class="btn" style="left:777px;top:1394px;width:98px;height:38px;line-height:36px;border:1.5px solid var(--green);color:#333">Join Now</div>

<!-- BEAUTY -->
<div class="band"></div>
<h2 class="sec-title serif" style="top:1584px;font-size:35px;font-weight:700;color:var(--ink)">Beauty Services</h2>
<p class="sec-title" style="top:1634px;font-size:11.5px;line-height:16.5px;padding:0 270px">Nam eu volutpat orci, quis accumsan dui. Curabitur finibus scelerisque dolor, non tincidunt nibh vehicula eu. Integer massa arcu, lobortis ac tincidunt vel, tincidunt eget orci Vestibulum ut consequat tellus</p>

<div class="abs" style="left:340px;top:1696px;width:520px;height:375px;overflow:hidden">
  <svg width="520" height="520" viewBox="0 0 520 520" style="position:absolute;left:0;top:0">
    <defs><linearGradient id="ring2" x1="0" y1="1" x2="1" y2="0"><stop offset="0" stop-color="#6ec3c9"/><stop offset="1" stop-color="#7ab55c"/></linearGradient></defs>
    <circle cx="260" cy="260" r="250" fill="none" stroke="url(#ring2)" stroke-width="6"/>
  </svg>
  <div class="photo" style="left:35px;top:35px;width:450px;height:450px;background:radial-gradient(circle at 60% 45%,#c9c3a4,#8c9a7a 45%,#e9ecec 80%)" role="img" aria-label="Woman receiving a clay facial mask treatment"></div>
</div>

<div class="svc" style="left:162px;top:1733px"><span class="disc"><i></i></span>Botox</div>
<div class="svc" style="left:162px;top:1913px"><span class="disc"><i></i></span>Skincare</div>
<div class="svc" style="left:906px;top:1733px"><span class="disc"><i></i></span>Fillers</div>
<div class="svc" style="left:904px;top:1913px"><span class="disc"><i></i></span>Microneedling</div>

<!-- EVENTS -->
<h2 class="sec-title serif" style="top:2133px;font-size:29px;font-weight:700;color:#333">Upcoming Events</h2>
<div class="event" style="left:188px"><div class="ph" style="background:radial-gradient(circle at 55% 40%,#c9a48a,#5b4c46 70%,#d9d9d9)" role="img" aria-label="Woman eating a fruit salad"></div>
  <h4>Lorem ipsum dolor sit amet,<br>consectetur adipi</h4><div class="when">Fernbrook, OhioMar 09 - 202008:00 am - 05:00 pm</div>
  <p>Nam eu volutpat orci, quis accumsan dui. Curabitur finibus scelerisque dolor, non tincidunt nibh vehicula eu. Integer massa arcu, lobortis ac tincidunt</p></div>
<div class="event" style="left:479px"><div class="ph" style="background:radial-gradient(circle at 50% 45%,#c5a08c,#3a3f48 60%,#9aa0a6)" role="img" aria-label="Woman stretching during a workout"></div>
  <h4>Lorem ipsum dolor sit amet,<br>consectetur adipi</h4><div class="when">Fernbrook, OhioMar 09 - 202008:00 am - 05:00 pm</div>
  <p>Nam eu volutpat orci, quis accumsan dui. Curabitur finibus scelerisque dolor, non tincidunt nibh vehicula eu. Integer massa arcu, lobortis ac tincidunt</p></div>
<div class="event" style="left:783px"><div class="ph" style="background:radial-gradient(circle at 50% 50%,#c9a43c,#7a9a3c 45%,#ddd 80%)" role="img" aria-label="Bowl of fresh vegetable salad"></div>
  <h4>Lorem ipsum dolor sit amet,<br>consectetur adipi</h4><div class="when">Fernbrook, OhioMar 09 - 202008:00 am - 05:00 pm</div>
  <p>Nam eu volutpat orci, quis accumsan dui. Curabitur finibus scelerisque dolor, non tincidunt nibh vehicula eu. Integer massa arcu, lobortis ac tincidunt</p></div>

<!-- SUCCESS STORIES -->
<div class="abs" style="left:0;top:2700px;width:1200px;height:673px;background:linear-gradient(180deg,#fff 0%,#eef4f8 55%,#f4f8fa 100%)"></div>
<div class="bubble" style="left:95px;top:2938px;width:115px;height:115px;background:radial-gradient(circle at 40% 40%,#f5fbff,#d6ebf6)"></div>
<div class="bubble" style="left:970px;top:2938px;width:115px;height:115px;background:radial-gradient(circle at 40% 40%,#fff,#e3eedb)"></div>

<div class="sec-title" style="top:2597px"><span class="script" style="font-size:27px;color:#333;margin-right:6px">Real People.</span><span class="serif" style="font-size:21px;font-weight:700;color:var(--navy)">Real Results.</span></div>
<h2 class="sec-title serif" style="top:2625px;font-size:42px;font-weight:700;color:var(--ink)">Success Stories</h2>
<p class="sec-title" style="top:2680px;font-size:12.5px;font-family:'Poppins',sans-serif;color:#444">Our clinics have helped thousands of patients lose weight &amp; feel great!</p>

<div class="story" style="left:168px;top:2730px;width:144px;height:144px"><div class="photo" style="left:8px;top:8px;width:118px;height:118px;background:radial-gradient(circle,#7a5346,#d7b9c9)" role="img" aria-label="Smiling woman in workout gear"></div></div>
<div class="story" style="left:333px;top:2726px;width:152px;height:152px"><div class="photo" style="left:8px;top:8px;width:126px;height:126px;background:radial-gradient(circle,#d6ab90,#ece4dd)" role="img" aria-label="Smiling woman with a healthy snack"></div></div>
<div class="story" style="left:509px;top:2712px;width:180px;height:180px"><div class="photo" style="left:9px;top:9px;width:152px;height:152px;background:radial-gradient(circle,#b9a9a0,#e2dcd8)" role="img" aria-label="Woman doing squats at home"></div></div>
<div class="story" style="left:707px;top:2726px;width:156px;height:156px"><div class="photo" style="left:8px;top:8px;width:130px;height:130px;background:radial-gradient(circle,#3b3a3f,#a7a986)" role="img" aria-label="Woman holding a yoga mat outdoors"></div></div>
<div class="story" style="left:885px;top:2730px;width:144px;height:144px"><div class="photo" style="left:8px;top:8px;width:118px;height:118px;background:radial-gradient(circle,#c9b3a3,#6f8fa6)" role="img" aria-label="Smiling older woman outdoors"></div></div>

<div class="btn btn-blue" style="left:487px;top:2926px;width:226px;height:42px;line-height:42px;font-size:12px">REAL RESULTS</div>

<div class="sec-title script" style="top:3030px;font-size:64px;color:#222">Get on the list</div>
<p class="sec-title" style="top:3117px;font-size:12.5px;font-family:'Poppins',sans-serif;color:#444">Sign up to receive news, updates and specials in your inbox!</p>
<div class="field" style="left:212px">FIRST NAME</div>
<div class="field" style="left:475px">LAST NAME</div>
<div class="field" style="left:739px">EMAIL ID</div>
<div class="btn" style="left:523px;top:3246px;width:154px;height:44px;line-height:44px;background:var(--green);font-family:'Poppins',sans-serif;font-size:15px;font-weight:600">Sign Up</div>

<!-- FOOTER -->
<footer class="footer">
  <div class="f-btn" style="left:161px;width:175px">
    <svg width="10" height="10" viewBox="0 0 24 24" style="vertical-align:-1px;margin-right:6px"><path fill="#fff" d="M6.6 10.8a15 15 0 0 0 6.6 6.6l2.2-2.2a1 1 0 0 1 1-.25 11.4 11.4 0 0 0 3.6.57 1 1 0 0 1 1 1V20a1 1 0 0 1-1 1A17 17 0 0 1 3 4a1 1 0 0 1 1-1h3.5a1 1 0 0 1 1 1 11.4 11.4 0 0 0 .57 3.6 1 1 0 0 1-.25 1z"/></svg>555.014.7788</div>
  <span class="social" style="left:516px"></span>
  <span class="social" style="left:561px"></span>
  <span class="social" style="left:606px"></span>
  <span class="social" style="left:651px"></span>
  <div class="f-btn" style="left:853px;width:185px;font-size:9.5px;letter-spacing:0">
    <svg width="11" height="9" viewBox="0 0 24 18" style="vertical-align:-1px;margin-right:5px"><rect x="1" y="1" width="22" height="16" rx="2" fill="none" stroke="#fff" stroke-width="2"/><path d="M1 2l11 8 11-8" fill="none" stroke="#fff" stroke-width="2"/></svg>INFO@BRIGHTOAKRX.EXAMPLE</div>
  <nav class="f-nav"><span>HOME</span><span>ABOUT US</span><span>OUR SERVICES</span><span>BLOG</span><span>CONTACT US</span></nav>
  <div class="f-rule"></div>
  <div class="copy">©2022 BRIGHTOAKRX. ALL RIGHTS RESERVED.</div>
</footer>

</body>
</html>
```